Tovimerra: Travel business card redesign

We need a clean elegant look for our cards featuring blue and orange. Look should communicate a sense of strong design and seem uncluttered. The company is Tovimerra which means escape to bliss. As in every trip is an escape to bliss. Feel free to reinvent the logo or just tweak it. Colors should be blue like Caribbean waters and a saturated orange. Keep it clean and simple.
Please match the information in the sample uploaded but the sample is horrible -- a non-starter -- use for information only. also please add managing director to my name as title

Target Market(s)
potential clients, hotels, trade publications
Industry/Entity Type
Travel Industry
Contact Information for Business Card
as above
Requirements
Must have
- Font should be century gothic. Colors below are close but a but prefer lighter in each case.

```html
<!DOCTYPE html>
<html lang="en">
<head>
<meta charset="utf-8">
<title>Tovimerra business cards</title>
<link rel="stylesheet" href="https://fonts.googleapis.com/css2?family=Mulish:wght@400;600;700&display=swap">
<style>
  :root {
    --bg: #3b3c3e;
    --white: #ffffff;
    --navy: #14304f;
    --deep-blue: #1d5f8c;
    --sea-blue: #2197cc;
    --bright-blue: #2aa6dc;
    --orange: #f0673a;
    --text-font: "Mulish", "Century Gothic", sans-serif;
  }
  * { margin: 0; padding: 0; box-sizing: border-box; }
  html, body { width: 1200px; height: 1000px; overflow: hidden; }
  body {
    background: var(--bg);
    font-family: var(--text-font);
    position: relative;
  }
  .card {
    position: absolute;
    width: 600px;
    height: 343px;
    background: var(--white);
    overflow: hidden;
  }
  .card--front { left: 300px; top: 110px; }
  .card--back  { left: 300px; top: 547px; }
  .card > svg { position: absolute; inset: 0; width: 100%; height: 100%; }

  .brand {
    position: absolute;
    display: flex;
    align-items: center;
    gap: 10px;
    color: var(--orange);
    font-weight: 700;
  }
  .brand__dot {
    width: 14px; height: 14px;
    border-radius: 50%;
    background: var(--bright-blue);
  }
  .card--front .brand { left: 0; right: 0; top: 128px; justify-content: center; font-size: 62px; letter-spacing: -1px; }
  .card--back .brand { left: 34px; top: 104px; font-size: 34px; }
  .card--back .brand__dot { width: 10px; height: 10px; }

  .front-url {
    position: absolute;
    left: 0; right: 0; bottom: 26px;
    display: flex; align-items: center; justify-content: center; gap: 14px;
    color: var(--white);
    font-size: 15px;
    letter-spacing: 0.5px;
  }
  .front-url::before, .front-url::after {
    content: ""; width: 50px; height: 1px; background: var(--white);
  }

  .contact {
    position: absolute;
    left: 412px; top: 64px;
    color: var(--white);
  }
  .contact__name { font-size: 18px; font-weight: 700; letter-spacing: 1px; white-space: nowrap; }
  .contact__title { font-size: 8px; font-weight: 700; letter-spacing: 1px; margin: 2px 0 12px; text-transform: uppercase; }
  .contact__list { list-style: none; font-size: 12px; line-height: 1.45; }
  .contact__list li { display: flex; align-items: flex-start; gap: 8px; white-space: nowrap; }
  .contact__icon {
    flex: none; width: 11px; height: 11px; margin-top: 3px;
    border-radius: 50%; background: var(--white);
    display: flex; align-items: center; justify-content: center;
  }
  .contact__icon svg { width: 7px; height: 7px; }
</style>
</head>
<body>

<section class="card card--front" aria-label="Card front">
  <svg viewBox="0 0 600 343" preserveAspectRatio="none" aria-hidden="true">
    <defs>
      <linearGradient id="frontWave" x1="0" y1="0" x2="1" y2="0">
        <stop offset="0" stop-color="var(--navy)"/>
        <stop offset="0.55" stop-color="var(--deep-blue)"/>
        <stop offset="1" stop-color="var(--bright-blue)"/>
      </linearGradient>
      <linearGradient id="frontTop" x1="0" y1="0" x2="1" y2="0">
        <stop offset="0" stop-color="var(--sea-blue)"/>
        <stop offset="1" stop-color="var(--deep-blue)"/>
      </linearGradient>
    </defs>
    <path d="M0,0 H600 V72 C440,22 240,6 0,26 Z" fill="url(#frontTop)"/>
    <path d="M0,34 C240,16 440,30 600,82" fill="none" stroke="var(--navy)" stroke-width="3"/>
    <path d="M0,200 C180,236 400,300 600,236 V343 H0 Z" fill="url(#frontWave)"/>
    <path d="M0,188 C180,224 400,288 600,224" fill="none" stroke="var(--navy)" stroke-width="5"/>
    <path d="M0,194 C180,230 400,294 600,230" fill="none" stroke="var(--white)" stroke-width="3"/>
  </svg>
  <div class="brand"><span class="brand__name">Tovimerra</span><span class="brand__dot"></span></div>
  <p class="front-url">www.tovimerra.com</p>
</section>

<section class="card card--back" aria-label="Card back">
  <svg viewBox="0 0 600 343" preserveAspectRatio="none" aria-hidden="true">
    <defs>
      <linearGradient id="backPanel" x1="0" y1="0" x2="1" y2="1">
        <stop offset="0" stop-color="var(--navy)"/>
        <stop offset="0.5" stop-color="var(--deep-blue)"/>
        <stop offset="1" stop-color="var(--bright-blue)"/>
      </linearGradient>
    </defs>
    <path d="M270,0 H600 V343 H0 V262 C130,268 260,256 396,252 Z" fill="url(#backPanel)"/>
    <path d="M0,236 C130,244 260,238 388,234" fill="none" stroke="var(--navy)" stroke-width="5"/>
    <path d="M0,250 C130,258 260,248 394,244" fill="none" stroke="var(--white)" stroke-width="3"/>
  </svg>
  <div class="brand"><span class="brand__name">Tovimerra</span><span class="brand__dot"></span></div>
  <div class="contact">
    <p class="contact__name">REID HALVORSEN</p>
    <p class="contact__title">Designation</p>
    <ul class="contact__list">
      <li><span class="contact__icon"><svg viewBox="0 0 10 10"><path d="M2,1 L4,1 L4.6,3.4 L3.4,4.2 C4,5.6 4.6,6.2 5.8,6.6 L6.6,5.4 L9,6 L9,8 C5,9 1,5 2,1 Z" fill="var(--navy)"/></svg></span>877.55.TOVIM (868460)</li>
      <li><span class="contact__icon"><svg viewBox="0 0 10 10"><rect x="3" y="1" width="4" height="8" rx="1" fill="var(--navy)"/></svg></span>310.555.0142</li>
      <li><span class="contact__icon"><svg viewBox="0 0 10 10"><rect x="1.5" y="3" width="7" height="4" fill="var(--navy)"/></svg></span>310.555.0142</li>
      <li><span class="contact__icon"><svg viewBox="0 0 10 10"><circle cx="5" cy="5" r="3.5" fill="none" stroke="var(--navy)" stroke-width="1.2"/></svg></span>www.tovimerra.com</li>
      <li><span class="contact__icon"><svg viewBox="0 0 10 10"><rect x="1.5" y="2.5" width="7" height="5" fill="none" stroke="var(--navy)" stroke-width="1.2"/></svg></span>info@tovimerra.com</li>
      <li><span class="contact__icon"><svg viewBox="0 0 10 10"><path d="M5,9 C2,5.5 2,4 2,3.5 A3,3 0 0 1 8,3.5 C8,4 8,5.5 5,9 Z" fill="var(--navy)"/></svg></span>4150 Coral Bay Road N.<br>Seaview, 90417</li>
    </ul>
  </div>
</section>

</body>
</html>
```